Computer company startup need wordpress template

I am looking for a new design that is fresh, bold and stands out from the crowd for an IT company called Torvane Computers. We specialise in consumer and small business IT.

It will have to be mobile friendly, viewable on all devices. I need a template that i can work with and that will give our site a professional look and feel but not look like every other site out there.

To see what text will be on final site, see www.torvanecomputers-demo.com.au, i will change wording, but it is pretty close to what it's meant to be.

I have supplied logo and the main colours on car, business cards etc is black, red (and shades thereof) and white.

I am visualiing some home page with "Welcome to Torvane Computers, how may we help you today?" then 4 cool looking buttons below which says:

1. Residential computer / network issues
2. Business computer / network issues
3. Home Networking
4. New home networking

These buttons will then take you to the correct page which i will flesh out from the template. All pages need have sections for my support links etc.

Website built from template will have 5-6 pages max.

If anyone need any additional direction, please send me a message and i will answer.

Target Market(s)

Consumer and small business (1-20 employees) customers

Industry/Entity Type

It Company

Requirements
Must have
• professional look and feel

```html
<!DOCTYPE html>
<html lang="en">
<head>
<meta charset="utf-8">
<title>Torvane Computers</title>
<link href="https://fonts.googleapis.com/css2?family=Roboto:wght@400;500;700&family=Oswald:wght@400;500&display=swap" rel="stylesheet">
<style>
:root{
  --red:#e8262d;
  --red-dark:#c81d23;
  --black:#0c0c0e;
  --charcoal:#1b1c1f;
  --navy:#0d1826;
  --navy-deep:#08101b;
  --white:#ffffff;
  --muted:#b9bcc2;
  --grey:#8a8d93;
}
*{margin:0;padding:0;box-sizing:border-box}
html,body{width:1200px;height:2328px;overflow:hidden;background:var(--black)}
body{position:relative;font-family:"Roboto",Arial,sans-serif;color:var(--white)}
section,header,footer{position:absolute;left:0;width:1200px}

.hero{top:0;height:720px;background:radial-gradient(ellipse at 70% 25%,#8a8f96 0%,#4e5257 35%,#24262a 70%,#141517 100%)}
.hero-photo{position:absolute;inset:0}
.main-nav{position:absolute;top:0;left:0;width:1200px;height:44px;background:rgba(0,0,0,.75);display:flex;justify-content:center;gap:86px;align-items:center}
.main-nav a{color:var(--white);text-decoration:none;font-size:21px;font-weight:500;letter-spacing:.5px}
.hero-welcome{position:absolute;top:118px;width:100%;text-align:center;font-size:50px;letter-spacing:2px}
.brand{position:absolute;top:180px;width:100%;display:flex;justify-content:center;align-items:center;gap:22px}
.brand-dot{width:34px;height:34px;border-radius:50%;background:var(--red)}
.brand-name{font-family:"Roboto",Arial,sans-serif;font-weight:700;font-size:92px;color:var(--red);letter-spacing:1px}

.services{top:720px;height:380px;background:linear-gradient(180deg,#1e1f23,#121316)}
.services h2{position:absolute;top:52px;width:100%;text-align:center;font-weight:400;font-size:38px}
.service-list{position:absolute;top:140px;left:148px;display:flex;gap:0}
.service{width:240px;text-align:center}
.service-icon{display:block;width:112px;height:92px;margin:0 auto 20px;border-radius:10px}
.service:nth-child(1) .service-icon{background:linear-gradient(160deg,#9fd4f2,#4c88b8)}
.service:nth-child(2) .service-icon{background:linear-gradient(160deg,#58a8dc,#1f5f95)}
.service:nth-child(3) .service-icon{background:linear-gradient(160deg,#e9ebee,#8e9399)}
.service:nth-child(4) .service-icon{background:linear-gradient(160deg,#c9dcef,#5c7fa6)}
.service p{font-size:27px;line-height:1.3;color:var(--white)}
.service.active p{color:var(--red)}

.call-band{top:1100px;height:188px;background:var(--red);display:flex;justify-content:center;align-items:center;gap:34px;font-family:"Oswald",Arial,sans-serif}
.call-label{font-size:44px;letter-spacing:1px}
.call-number{font-size:48px;letter-spacing:1px}

.testimonials{top:1288px;height:424px;background:radial-gradient(ellipse at 50% 45%,#17273b 0%,var(--navy) 55%,var(--navy-deep) 100%);text-align:center}
.testimonials h2{position:absolute;top:42px;width:100%;font-family:"Oswald",Arial,sans-serif;font-weight:400;font-size:50px;color:var(--red);letter-spacing:1px}
.quote-mark{position:absolute;top:108px;width:100%;font-family:"Oswald",Arial,sans-serif;font-size:80px;line-height:1;color:var(--red)}
.quote-text{position:absolute;top:200px;left:180px;width:840px;font-size:18px;line-height:1.6;color:var(--white)}
.quote-author{position:absolute;top:300px;width:100%;font-size:18px;color:var(--red)}
.dots{position:absolute;top:334px;width:100%;display:flex;justify-content:center;gap:12px}
.dots span{width:16px;height:16px;border-radius:50%;background:var(--white)}
.dots span.on{background:var(--red)}

.remote{top:1712px;height:236px;background:linear-gradient(180deg,#2a2b2f,#18191c)}
.remote-icon{position:absolute;top:54px;left:300px;width:104px;height:104px;border-radius:14px;background:linear-gradient(160deg,#4aa3e6,#1a6bb5)}
.remote p{position:absolute;top:70px;left:400px;width:560px;font-size:24px;line-height:1.5}

.site-footer{top:1948px;height:332px;background:var(--black)}
.footer-col{position:absolute;top:24px}
.footer-col h3{font-weight:400;font-size:34px;margin-bottom:20px}
.links{left:78px}
.links ul{list-style:none}
.links li{font-size:17px;line-height:31px;color:var(--white)}
.links li.current{color:var(--red)}
.news{left:444px;width:330px}
.news-item{margin-bottom:14px}
.news-date{font-size:13px;color:var(--grey)}
.news-title{font-size:21px;color:var(--red);margin:2px 0}
.news-text{font-size:15px;line-height:1.35}
.contact{left:810px}
.contact ul{list-style:none}
.contact li{display:flex;align-items:center;gap:14px;font-size:15px;line-height:30px}
.contact svg{flex:none}
.social{position:absolute;top:250px;left:810px;display:flex;gap:34px}
.social span{width:44px;height:44px;border-radius:50%;border:2px solid var(--red)}

.bottom-bar{top:2280px;height:48px;background:#050506;display:flex;justify-content:center;align-items:center;font-size:15px}
.bottom-bar b{color:var(--red);font-weight:500}
</style>
</head>
<body>

<header class="hero">
  <div class="hero-photo" role="img" aria-label="Photo of hands on a laptop keyboard beside a computer mouse"></div>
  <nav class="main-nav">
    <a href="#">HOME</a><a href="#">ABOUT</a><a href="#">SERVICES</a><a href="#">FAQ</a><a href="#">CONTACT</a>
  </nav>
  <div class="hero-welcome">WELCOME TO</div>
  <div class="brand"><span class="brand-dot"></span><span class="brand-name">Torvane Computers</span></div>
</header>

<section class="services">
  <h2>How may we help you today?</h2>
  <div class="service-list">
    <div class="service active"><span class="service-icon" role="img" aria-label="Illustration of a home computer"></span><p>Residential computer<br>/ network issues</p></div>
    <div class="service"><span class="service-icon" role="img" aria-label="Illustration of a business network"></span><p>Business computer /<br>network issues</p></div>
    <div class="service"><span class="service-icon" role="img" aria-label="Illustration of a house"></span><p>Home<br>Networking</p></div>
    <div class="service"><span class="service-icon" role="img" aria-label="Illustration of a new house with network"></span><p>New Home<br>networking</p></div>
  </div>
</section>

<section class="call-band">
  <span class="call-label">CALL US ON :</span>
  <svg width="64" height="64" viewBox="0 0 64 64" aria-hidden="true">
    <circle cx="32" cy="32" r="29" fill="none" stroke="#fff" stroke-width="3"/>
    <path d="M23 18c2-1 4 0 5 2l2 5c1 2 0 3-1 4l-2 2c2 4 5 7 9 9l2-2c1-1 3-2 4-1l5 2c2 1 3 3 2 5l-1 3c-1 2-3 3-5 3-12-1-22-11-23-23 0-2 1-4 3-5z" fill="#fff"/>
  </svg>
  <span class="call-number">0491 570 118</span>
</section>

<section class="testimonials">
  <h2>YES, PEOPLE TALK ABOUT US</h2>
  <div class="quote-mark">&ldquo;</div>
  <p class="quote-text">Lorem Ipsum is simply dummy text of the printing and typesetting industry. Lorem Ipsum has been the industry's standard dummy text ever since the 1500s, when an unknown printer took a galley of type and scrambled it to make a type specimen book.</p>
  <div class="quote-author">- Client Name</div>
  <div class="dots"><span class="on"></span><span></span><span></span><span></span></div>
</section>

<section class="remote">
  <div class="remote-icon" role="img" aria-label="Remote assistance software icon"></div>
  <p>If requested by our staff to do so, please click on this link to start our Remote Assistance Software.</p>
</section>

<footer class="site-footer">
  <div class="footer-col links">
    <h3>Useful Links</h3>
    <ul><li class="current">Home</li><li>About</li><li>Services</li><li>Faq</li><li>News</li><li>Contact</li></ul>
  </div>
  <div class="footer-col news">
    <h3>Latest News</h3>
    <div class="news-item"><div class="news-date">20 Aug 2015</div><div class="news-title">News Title</div><div class="news-text">Lorem Ipsum is simply dummy text of the printing and typesetting industry.</div></div>
    <div class="news-item"><div class="news-date">14 Aug 2015</div><div class="news-title">News Title</div><div class="news-text">Lorem Ipsum is simply dummy text of the printing and typesetting industry.</div></div>
  </div>
  <div class="footer-col contact">
    <h3>Contact Info</h3>
    <ul>
      <li><svg width="16" height="20" viewBox="0 0 16 20"><path d="M8 0a7 7 0 0 0-7 7c0 5 7 13 7 13s7-8 7-13a7 7 0 0 0-7-7zm0 10a3 3 0 1 1 0-6 3 3 0 0 1 0 6z" fill="#e8262d"/></svg>14 Harbour Close<br>Seaview Bay TAS 7000</li>
      <li><svg width="16" height="16" viewBox="0 0 16 16"><path d="M3 1c1 0 2 2 2 3s-1 1-1 2c1 2 3 4 5 5 1 0 1-1 2-1s3 1 3 2-1 3-3 3C6 15 1 10 1 4c0-2 1-3 2-3z" fill="#e8262d"/></svg>0491 570 118</li>
      <li><svg width="18" height="14" viewBox="0 0 18 14"><rect x="1" y="1" width="16" height="12" fill="none" stroke="#e8262d" stroke-width="2"/><path d="M1 1l8 7 8-7" fill="none" stroke="#e8262d" stroke-width="2"/></svg>info@torvanecomputers-demo.com.au</li>
      <li><svg width="16" height="16" viewBox="0 0 16 16"><circle cx="8" cy="8" r="7" fill="none" stroke="#e8262d" stroke-width="2"/><path d="M1 8h14M8 1c3 3 3 11 0 14M8 1c-3 3-3 11 0 14" fill="none" stroke="#e8262d" stroke-width="1.5"/></svg>www.torvanecomputers-demo.com.au</li>
    </ul>
  </div>
  <div class="social"><span></span><span></span><span></span></div>
</footer>

<div class="bottom-bar" style="position:absolute;left:0;width:1200px;top:2280px"><span>&copy; <b>Torvane Computers</b> 2015. All Rights Reserved.</span></div>

</body>
</html>
```